Tri-Fold Menu of Services for our Eyelash and Skin Care Spa

We need a beautiful spa service menu for our upscale spa in St. Charles Missouri. We specialize in providing treatments that are specific to the clients needs. Our services are eyelash extensions, skin care treatments, full body waxing and makeup application. Our spa colors are dark purples and greys and we are not opposed to additional colors that would complement those colors. We do a lot of eyelash extensions and while we do what those services listed we would like the skin care treatments to be in an area that would be noticed first. One of the attachments lists all of our services, descriptions and prices (please be sure to include all services and pricing. descriptions if possible). And our website has more information about us if needed. The website was not professionally done. So it DOESN'T represent our style exactly.

I HAVE ATTACHED A FEW PHOTOS BUT THEY DON'T HAVE TO BE USED.

Target Market(s)

women who would like to look their best, 35-55, annual income of 100,000+, she is usually busy and her children (if she has any) are high school age or older.

Industry/Entity Type

It Service

Font styles to use
Serif
Sans Serif

Requirements
Must have
• Must list all of our services. If it works to have the descriptions that would be great.
Nice to have
• If it works to have the descriptions of each service that would be great.

```html
<!DOCTYPE html>
<html lang="en">
<head>
<meta charset="utf-8">
<title>Spa Menu of Services</title>
<link href="https://fonts.googleapis.com/css2?family=Cormorant+SC:wght@500&family=PT+Sans:wght@400;700&display=swap" rel="stylesheet">
<style>
  :root {
    --plum: #6a2c5f;
    --ink: #2e2a2c;
    --paper: #ffffff;
    --swoosh: #e3e0e2;
    --swoosh-deep: #c9c4c8;
    --skin-light: #f3e2d8;
    --skin-mid: #e6bfa8;
    --skin-deep: #d2a08a;
  }
  * { margin: 0; padding: 0; box-sizing: border-box; }
  html, body { width: 1200px; height: 927px; overflow: hidden; background: var(--paper); }
  body { font-family: "PT Sans", Arial, sans-serif; color: var(--ink); }
  .menu { position: relative; width: 1200px; height: 927px; overflow: hidden; background: var(--paper); }
  .swooshes { position: absolute; inset: 0; z-index: 0; }
  .model-photo { position: absolute; left: 880px; top: 590px; width: 320px; height: 337px; z-index: 1;
    background:
      radial-gradient(ellipse 42% 48% at 60% 52%, var(--skin-deep) 0%, var(--skin-mid) 45%, rgba(230,191,168,0) 100%),
      radial-gradient(ellipse 70% 80% at 62% 55%, var(--skin-light) 0%, rgba(243,226,216,0.6) 55%, rgba(255,255,255,0) 100%); }
  .column { position: absolute; z-index: 2; }
  .col-facial { left: 45px; top: 44px; width: 372px; }
  .col-peels { left: 444px; top: 44px; width: 370px; }
  .col-lashes { left: 844px; top: 44px; width: 320px; }
  .section-title { font-family: "Cormorant SC", Georgia, serif; font-weight: 500; color: var(--plum);
    font-size: 25px; letter-spacing: 1.5px; line-height: 1; margin-bottom: 20px; }
  .treatment { margin-bottom: 12px; }
  .treatment-name { font-weight: 700; color: var(--plum); font-size: 14.5px; line-height: 1.25; }
  .treatment-name .price { color: var(--ink); margin-left: 4px; }
  .treatment-desc { font-size: 12.4px; line-height: 1.3; margin-top: 3px; }
  .col-facial .treatment-desc { font-size: 13.2px; line-height: 15.6px; }
  .package-line { display: flex; justify-content: space-between; font-size: 13.2px; line-height: 15.6px; }
  .package-line b { font-weight: 700; }
  .peel { margin-bottom: 16px; }
  .peel-head { display: flex; font-size: 14.5px; line-height: 1.25; }
  .peel-head .treatment-name { width: 232px; }
  .peel-head .price { font-size: 12.4px; font-weight: 700; color: var(--ink); padding-top: 2px; }
  .price-list { list-style: none; font-size: 12.4px; line-height: 17px; }
  .price-list li { display: flex; }
  .price-list .item { width: 218px; }
  .col-lashes .price-list .item { width: 167px; }
  .list-group { font-weight: 700; color: var(--plum); font-size: 14.5px; line-height: 18px; }
  .addons { margin-top: 34px; }
  .massages { margin-top: 44px; }
  .massage-note { font-size: 12.4px; line-height: 1.3; width: 330px; }
  .waxing { margin-top: 30px; }
  .tinting { margin-top: 30px; }
</style>
</head>
<body>
<main class="menu">
  <svg class="swooshes" width="1200" height="927" viewBox="0 0 1200 927" aria-hidden="true">
    <defs>
      <linearGradient id="swoosh-fade" x1="0" y1="0" x2="1" y2="0">
        <stop offset="0" stop-color="#d6d2d5" stop-opacity="0"/>
        <stop offset="0.35" stop-color="#d6d2d5" stop-opacity="0.8"/>
        <stop offset="1" stop-color="#bdb7bb" stop-opacity="0.9"/>
      </linearGradient>
    </defs>
    <path d="M425 600 Q 700 598 1000 662 Q 700 620 425 607 Z" fill="url(#swoosh-fade)"/>
    <path d="M0 927 L0 880 Q 300 800 620 818 Q 900 835 1200 800 L1200 927 Z" fill="var(--swoosh)" opacity="0.6"/>
    <path d="M0 905 Q 320 830 640 845 Q 900 858 1200 830" fill="none" stroke="var(--swoosh-deep)" stroke-width="2"/>
  </svg>

  <div class="model-photo" role="img" aria-label="Photo of a woman with eyes closed having powder applied with a makeup brush"></div>

  <section class="column col-facial">
    <h2 class="section-title">Facial &amp; Skin Treatments</h2>
    <article class="treatment">
      <h3 class="treatment-name">Luminelle Lift &amp; Glow Treatment Facial <span class="price">$95 60 mins</span></h3>
      <p class="treatment-desc" style="margin-top:12px">Seeking a treatment with amazing instant results? Redefining radiance and facial contouring, this exclusively formulated treatment features the latest in freezedried technology to deliver instant results and cumulative skin care benefits. Ideal for any skin type showing signs of aging,or as the perfect in-stant repair boost when you want to look your best. Proven to perform, the Verdessa Luminelle Lift &amp; Glow facial renders your skin ultraluminous with a firmer, tighter, and more youthfully defined appearance.</p>
    </article>
    <article class="treatment" style="margin-top:16px">
      <h3 class="treatment-name">Soothing Calmaris Treatment Facial <span class="price">$100 60 mins</span></h3>
      <p class="treatment-desc">This highly effective, soothing treatment calms redness and alleviates irritated or sensitive skin. A healing Propolis ampoule (natural ingredient collected by bees) is applied to desensitize the skin's surface and strengthen capillaries. A cooling liftoff mask is then applied to seal in the vitamin enriched beneficial ampoule.</p>
    </article>
    <article class="treatment" style="margin-top:16px">
      <h3 class="treatment-name">Radiance PhotoTherapy Treatment <span class="price">$150 Package</span></h3>
      <p class="treatment-desc" style="margin-top:12px">Uses heat and light energy to gently break up areas of excess pigment while stimulating the production of new collagen. Improved skin tone, less spots, fewer pink areas, less redness, reduction in fine lines and wrinkles. Diminishes pores and restores natural radiant glow of skin. Like laser treatments MicroPhotoTherapy treats skin with therapeutic light energy but unlike laser treatments, Micro PhotoTherapy features gentle waves of heat and light that improve the skin with no downtime and very little discomfort.<br>We recommend 8 treatments 1 to 2 times a week for best</p>
      <p class="package-line"><span>results.</span><b>8 treatments $800</b></p>
    </article>
    <article class="treatment" style="margin-top:10px">
      <h3 class="treatment-name">Diamond Microdermabrasion Treatment <span class="price" style="margin-left:24px">$78</span></h3>
      <p class="treatment-desc">With this treatment you will see softening of fine lines and wrinkles and smoothing of coarsely textured skin. Dull, stressed or congested skin will be brighter and clearer. The appearance of enlarged pores, and acne scars will be minimized. Your at home products will be able to penetrate deeper therefore, are more effective. Or add this to any facial or most peels for just $30.</p>
    </article>
  </section>

  <section class="column col-peels">
    <h2 class="section-title">Peels</h2>
    <article class="peel">
      <div class="peel-head"><h3 class="treatment-name">Acne Lift Peel</h3><span class="price">$50/1 $250/6 30 mins</span></div>
      <p class="treatment-desc">Mild to moderate Acne peel</p>
    </article>
    <article class="peel">
      <div class="peel-head"><h3 class="treatment-name">Lightening Lift Peel</h3><span class="price">$50/1 $250/6</span></div>
      <p class="treatment-desc" style="margin-top:0"><b>30 mins</b><br>Pigmentation (sun/brown spots), uneven skin tone</p>
    </article>
    <article class="peel">
      <div class="peel-head"><h3 class="treatment-name">Wrinkle Lift</h3><span class="price">$50/1 $250/6 30 mins</span></div>
      <p class="treatment-desc">Aging, fine lines and wrinkles</p>
    </article>
    <article class="peel">
      <div class="peel-head"><h3 class="treatment-name">Signature Lift</h3><span class="price">$50/1 $250/6 30 mins</span></div>
      <p class="treatment-desc">Rosacea, dry/dehydrated</p>
    </article>
    <article class="peel">
      <div class="peel-head"><h3 class="treatment-name">Perfection Lift</h3><span class="price">$100/1 $350/4 30 mins</span></div>
      <p class="treatment-desc" style="margin-top:0">Advanced Aging, Acne, and Pigmentation (slightly more aggressive than the other options)</p>
    </article>

    <div class="addons">
      <h2 class="section-title">Add Ons</h2>
      <ul class="price-list">
        <li><span class="item">Microdermabrasion</span><span>$30</span></li>
        <li><span class="item">Luminelle Lift &amp; Glow Eye Treatment</span><span>$20</span></li>
        <li><span class="item">Hot or Cold Stones</span><span>$15</span></li>
        <li><span class="item">Extended Massage</span><span>$15</span></li>
        <li><span class="item">Peppermint Scalp Massage</span><span>$15</span></li>
        <li><span class="item">Foot Scrub &amp; Massage</span><span>$20</span></li>
        <li><span class="item">Aromatherapy</span><span>$10</span></li>
        <li><span class="item">Specialty Ampoule</span><span>$15</span></li>
        <li><span class="item">Specialty Mask</span><span>$13</span></li>
      </ul>
    </div>

    <div class="massages">
      <h2 class="section-title">Massages &amp; Scrubs</h2>
      <ul class="price-list" style="line-height:15.5px">
        <li><span class="item">Neck, Back &amp; Head Massage</span><span>$45 (30 mins)</span></li>
        <li><span class="item">Aromatherapy Scalp Massage</span><span>$15 (10 mins)</span></li>
        <li><span class="item">Foot Massage and Scrub</span><span>$20 (15 mins)</span></li>
        <li><span class="item">Headache &amp; Migraine Relief Treatment</span><span>$45 (30 mins)</span></li>
      </ul>
      <p class="massage-note">(Relief from headaches caused by stress, tension, hormonal imbalances orsensitivities using cold stones and massaging techniques for the face.</p>
    </div>
  </section>

  <section class="column col-lashes">
    <h2 class="section-title">Eyelashes</h2>
    <ul class="price-list">
      <li class="list-group">Classic</li>
      <li><span class="item">Full Set</span><span>$175</span></li>
      <li><span class="item">Demi Set</span><span>$110</span></li>
      <li><span class="item">Touch up</span><span>$60</span></li>
      <li class="list-group">Volume Technique</li>
      <li><span class="item">Full Set</span><span>$220</span></li>
      <li><span class="item">Demi Set</span><span>$135</span></li>
      <li><span class="item">Touch up</span><span>$72</span></li>
    </ul>

    <div class="waxing">
      <h2 class="section-title">Waxing</h2>
      <ul class="price-list">
        <li><span class="item">Eyebrows</span><span>$17</span></li>
        <li><span class="item">Upper Lip</span><span>$14</span></li>
        <li><span class="item">Chin</span><span>$14</span></li>
        <li><span class="item">Sides of face</span><span>$14</span></li>
        <li><span class="item">Bikini</span><span>$27+</span></li>
        <li><span class="item">Brazilian</span><span>$55+</span></li>
        <li><span class="item">Underarm</span><span>$22</span></li>
        <li><span class="item">Arms</span><span>Full $35 Lower $26</span></li>
        <li><span class="item">Legs</span><span>Full $62 Lower $40</span></li>
        <li><span class="item">Chest</span><span>$44</span></li>
        <li><span class="item">Back</span><span>$44</span></li>
      </ul>
    </div>

    <div class="tinting">
      <h2 class="section-title">Tinting</h2>
      <ul class="price-list">
        <li><span class="item">eyebrows</span><span>$20</span></li>
        <li><span class="item">eyelashes</span><span>$20</span></li>
        <li><span class="item">both</span><span>$30</span></li>
      </ul>
    </div>
  </section>
</main>
</body>
</html>
```